Darrow Consulting needs a quality & professional business card!

I am a recruitment and employment consultant from Brisbane, Australia and I had a fantastic logo organised by this community to I am hoping the business card will be the same.

I have attached the Darrow consulting logo that ideally would feature on the back of the business card. There are a number of logos for you to use as you see fit. I would like the colour cheme to match that of the Darrow Consulting logo. I also have a secondary company called Career Lantern Australia and I have included that logo as well. While it is an important part of the business I don't want this logo feature too predominantly as I am moving out of this space. This logo was created by myself and is of low quality. Feel free to use the icon and words however you want. The winning design will be smart, professional and eye-catching.

The information I am looking for in the business card is:
Name: Gavin Darrow
Position: Founder & Director
Phone: (07) 3519 6482
Mobile: 0431 586 207
Email: gavin@careerlantern.com.au

Target Market(s)

Recruiters, government, large companies

Contact Information for Business Card

Name: Gavin Darrow
Phone: (07) 3519 6482
Mobile: 0431 586 207
Web: www.careerlantern.com.au

Font styles to use
Serif
Sans Serif

Requirements
Must have
• Darrow Consulting Logo on reverse side
• Contact details on front side with smaller reference to Darrow Consulting logo and Career Lantern Australia logo

```html
<!DOCTYPE html>
<html lang="en">
<head>
<meta charset="utf-8">
<title>Darrow Consulting — Business Card</title>
<link rel="stylesheet" href="https://fonts.googleapis.com/css2?family=Open+Sans:wght@400;600;700&display=swap">
<style>
  :root {
    --backdrop: #3b3431;
    --card: #1b1c1e;
    --ink: #ffffff;
    --muted: #8d8f93;
    --accent: #1f9ad6;
    --rule: #e9e9e9;
  }
  * { margin: 0; padding: 0; box-sizing: border-box; }
  html, body { width: 1200px; height: 864px; overflow: hidden; }
  body {
    background: var(--backdrop);
    font-family: "Open Sans", Arial, sans-serif;
    position: relative;
  }
  .card {
    position: absolute;
    width: 520px;
    height: 316px;
    background: var(--card);
    border-radius: 3px;
    box-shadow: 0 12px 30px rgba(0,0,0,.45);
    color: var(--ink);
  }
  /* reverse side */
  .card--back { left: 60px; top: 110px; }
  .brand-mark {
    position: absolute;
    left: 0; right: 0; top: 96px;
    display: flex; align-items: center; justify-content: center; gap: 14px;
  }
  .brand-mark__square {
    width: 22px; height: 22px; background: var(--muted);
  }
  .brand-mark__name {
    font-weight: 600;
    font-size: 30px;
    color: var(--muted);
    letter-spacing: .5px;
  }
  .back-url {
    position: absolute;
    left: 0; right: 0; top: 208px;
    text-align: center;
    font-size: 12px;
    letter-spacing: 5px;
    color: var(--muted);
  }
  /* front side */
  .card--front { left: 620px; top: 420px; }
  .company-name {
    position: absolute; right: 34px; top: 68px;
    font-weight: 600; font-size: 19px; line-height: 1.2;
    color: var(--ink);
    white-space: nowrap;
  }
  .holder { position: absolute; left: 30px; top: 118px; }
  .holder__name {
    font-size: 17px; font-weight: 700; color: var(--accent);
    text-transform: uppercase; letter-spacing: .3px; line-height: 1.1;
  }
  .holder__role {
    font-size: 13px; font-weight: 700; color: var(--ink);
    text-transform: uppercase; line-height: 1.3;
  }
  .divider {
    position: absolute; left: 30px; right: 30px; top: 162px;
    height: 1.5px; background: var(--rule);
  }
  .contacts {
    position: absolute; left: 30px; top: 172px;
    list-style: none;
  }
  .contacts li {
    display: flex; align-items: center; gap: 7px;
    font-size: 13px; line-height: 19px; color: var(--ink);
  }
  .contacts svg { width: 11px; height: 11px; fill: var(--accent); flex: none; }
</style>
</head>
<body>

  <section class="card card--back" aria-label="Business card reverse">
    <div class="brand-mark">
      <div class="brand-mark__square"></div>
      <div class="brand-mark__name">Darrow Consulting</div>
    </div>
    <p class="back-url">www.careerlantern.com.au</p>
  </section>

  <section class="card card--front" aria-label="Business card front">
    <p class="company-name">Career Lantern Australia</p>

    <div class="holder">
      <p class="holder__name">Gavin Darrow</p>
      <p class="holder__role">Founder &amp; Director</p>
    </div>

    <div class="divider"></div>

    <ul class="contacts">
      <li>
        <svg viewBox="0 0 24 24" aria-hidden="true"><path d="M6.6 10.8a15.1 15.1 0 0 0 6.6 6.6l2.2-2.2c.3-.3.7-.4 1-.2 1.1.4 2.3.6 3.6.6.6 0 1 .4 1 1V20c0 .6-.4 1-1 1A17 17 0 0 1 3 4c0-.6.4-1 1-1h3.5c.6 0 1 .4 1 1 0 1.3.2 2.5.6 3.6.1.3 0 .7-.2 1z"/></svg>
        (07) 3519 6482
      </li>
      <li>
        <svg viewBox="0 0 24 24" aria-hidden="true"><path d="M7 1h10a2 2 0 0 1 2 2v18a2 2 0 0 1-2 2H7a2 2 0 0 1-2-2V3a2 2 0 0 1 2-2zm0 3v14h10V4zm5 15.5a1 1 0 1 0 0 2 1 1 0 0 0 0-2z"/></svg>
        0431 586 207
      </li>
      <li>
        <svg viewBox="0 0 24 24" aria-hidden="true"><path d="M2 5h20v14H2zm2 2v.5l8 5 8-5V7l-8 5z"/></svg>
        gavin@careerlantern.com.au
      </li>
      <li>
        <svg viewBox="0 0 24 24" aria-hidden="true"><path d="M12 2a10 10 0 1 0 0 20 10 10 0 0 0 0-20zm-1 17.9A8 8 0 0 1 4.1 11H8c.1 3.3 1.2 6.5 3 8.9zM8 9H4.1A8 8 0 0 1 11 4.1C9.2 6.5 8.1 9 8 9zm5 10.9c1.8-2.4 2.9-5.6 3-8.9h3.9a8 8 0 0 1-6.9 8.9zM16 9c-.1-.2-1.2-2.5-3-4.9A8 8 0 0 1 19.9 9z"/></svg>
        www.careerlantern.com.au
      </li>
    </ul>
  </section>

</body>
</html>
```